Redesign website for small print company

Vindaborgprent is a small printing company in Iceland mainly servicing Students, schools, etc. We are also doing all kind of other jobs, like business cards, book printing, brochure printing etc. We are also selling books online.
Our website is: www.vindaborgprent.is
What we are looking for is:
- Web Design (Uncoded - PSD layout only)
- Mobile friendly design, using our current color scheme: Red, green, yellow and light gray.
- Clean simple design
- Simple, light and easy to use.
- More menu Items/drop down
Industry/Entity Type
Digital Printing
Number of Pages Required
5+ page
Requirements
Must have
- Easy navigation
- Designed for mobile
- Current color scheme (see logo)
Nice to have
- Icon based products

```html
<!DOCTYPE html>
<html lang="en">
<head>
<meta charset="utf-8">
<title>Products &amp; Services</title>
<link href="https://fonts.googleapis.com/css2?family=Roboto:wght@700;900&family=Lato:wght@400&display=swap" rel="stylesheet">
<style>
  :root {
    --red: #ee3a2f;
    --yellow: #ffd400;
    --ink: #333333;
    --card-bg: #f5f5f5;
    --card-border: #dddddd;
    --icon-fill: #d6d6d7;
    --page: #ffffff;
  }
  * { box-sizing: border-box; margin: 0; padding: 0; }
  html, body { width: 1200px; height: 845px; overflow: hidden; background: var(--page); }
  .services {
    position: relative;
    width: 1200px;
    height: 845px;
    font-family: "Lato", sans-serif;
    color: var(--ink);
  }
  .services__title {
    position: absolute;
    top: 47px;
    left: 0;
    width: 100%;
    text-align: center;
    font-family: "Roboto", sans-serif;
    font-weight: 900;
    font-size: 43px;
    line-height: 54px;
    color: var(--red);
  }
  .services__title .accent { color: var(--yellow); }
  .services__intro {
    position: absolute;
    top: 111px;
    left: 0;
    width: 100%;
    text-align: center;
    font-size: 16px;
    line-height: 24px;
  }
  .service-grid {
    position: absolute;
    top: 202px;
    left: 143px;
    display: grid;
    grid-template-columns: repeat(3, 286px);
    grid-auto-rows: 278px;
    column-gap: 28px;
    row-gap: 29px;
  }
  .service-card {
    position: relative;
    background: var(--card-bg);
    border: 1px solid var(--card-border);
  }
  .service-card__icon {
    position: absolute;
    top: 62px;
    left: 50%;
    height: 96px;
    transform: translateX(-50%);
    background: var(--icon-fill);
  }
  .icon--essays { width: 76px; }
  .icon--cards { width: 150px; }
  .icon--leaflets { width: 82px; }
  .icon--books { width: 83px; }
  .icon--posters { width: 115px; }
  .icon--textbooks { width: 73px; }
  .service-card__name {
    position: absolute;
    top: 204px;
    left: 0;
    width: 100%;
    text-align: center;
    font-family: "Roboto", sans-serif;
    font-weight: 700;
    font-size: 22.5px;
    line-height: 28px;
    color: var(--ink);
  }
</style>
</head>
<body>
<section class="services">
  <h1 class="services__title">PRODUCTS &amp; <span class="accent">SERVICES</span></h1>
  <p class="services__intro">This is Pixelmora's version&nbsp; of Lorem Ipsum. Proin gravida nibh vel velit auctor aliquet.<br>Aenean sollicitudin, lorem quis bibendum auctor</p>

  <div class="service-grid">
    <article class="service-card">
      <div class="service-card__icon icon--essays" role="img" aria-label="Essay page icon"></div>
      <h2 class="service-card__name">ESSAYS</h2>
    </article>
    <article class="service-card">
      <div class="service-card__icon icon--cards" role="img" aria-label="Business cards icon"></div>
      <h2 class="service-card__name">BUSINESS CARDS</h2>
    </article>
    <article class="service-card">
      <div class="service-card__icon icon--leaflets" role="img" aria-label="Leaflets icon"></div>
      <h2 class="service-card__name">LEAFLETS</h2>
    </article>
    <article class="service-card">
      <div class="service-card__icon icon--books" role="img" aria-label="Book printing icon"></div>
      <h2 class="service-card__name">BOOK PRINTING</h2>
    </article>
    <article class="service-card">
      <div class="service-card__icon icon--posters" role="img" aria-label="Poster icon"></div>
      <h2 class="service-card__name">POSTERS</h2>
    </article>
    <article class="service-card">
      <div class="service-card__icon icon--textbooks" role="img" aria-label="Textbook icon"></div>
      <h2 class="service-card__name">TEXTBOOKS</h2>
    </article>
  </div>
</section>
</body>
</html>
```